Website for "Bright Meadow Ltd" cleaning bsuiness

We require a website to expose our business to the local market. We want to provide background on who we are and what we do but in an easily digestible way. We clean domestic and commercial premises and want to provide a list of all of our services to potential customers. We operate out of Ashbridge in the UK.

We would like the website to be animated in some way so that the experience of using it is not dull or mundane. This website needs to be an extension of our company.

Target Market(s)

30 - 60 year olds for Domestic plus commercial clients

Industry/Entity Type

Cleaning Service

Coding

Coded - Design and coding required

Number of Pages Required

4 page

Font styles to use
Sans Serif

Colors
0455a3
3176b5
85acd3
cfdeed
ffffff
000000
1b1b1b
c8c8c8
757575

Requirements
Must have
• Logo which has been provided. Theme based around the logo and its colours. Simple layout to avoid confusion.
Nice to have
• Animations where possible to impress the customer.
Should not have
• any pictures of cleaning equipment, fairies, maids etc

```html
<!DOCTYPE html>
<html lang="en">
<head>
<meta charset="utf-8">
<title>Bright Meadow Ltd – Cleaning Services, Ashbridge</title>
<link href="https://fonts.googleapis.com/css2?family=Roboto:wght@400;500;700&family=Carlito:wght@400;700&display=swap" rel="stylesheet">
<style>
  :root{
    --cyan:#1cb9e8;
    --cyan-light:#27c4f0;
    --silver:#3176b5;
    --gold:#0455a3;
    --ink:#1b1b1b;
    --grey:#757575;
    --rule:#c8c8c8;
    --panel:#f4f4f4;
    --white:#ffffff;
  }
  *{box-sizing:border-box;margin:0;padding:0}
  html,body{width:780px;height:1200px;overflow:hidden;background:var(--white)}
  body{position:relative;font-family:"Carlito",Calibri,sans-serif;color:var(--ink)}
  .abs{position:absolute}
  .section-title{position:absolute;left:0;width:780px;text-align:center;font-family:"Roboto",sans-serif;font-weight:500;font-size:14px;color:#2a2a2a;letter-spacing:.1px}
  .wave{position:absolute;width:40px;height:6px}

  /* testimonials */
  .testimonials{left:0;top:0;width:780px;height:108px;background:linear-gradient(100deg,#5ccfee 0%,#46c2ea 40%,#6fd3ef 70%,#57c8ec 100%)}
  .avatar{position:absolute;width:46px;height:46px;border-radius:50%;background:#d9e8ee;border:2px solid rgba(255,255,255,.8)}
  .reviewer{position:absolute;color:var(--white);font-family:"Roboto",sans-serif;font-size:8px;font-weight:700;text-transform:uppercase}
  .reviewer span{display:block;text-transform:none;font-weight:400;font-size:7.5px;margin-top:1px}
  .dot{position:absolute;top:66px;width:5px;height:5px;border-radius:50%;background:rgba(255,255,255,.85)}
  .dot.active{background:transparent;border:1px solid #fff}

  /* clients */
  .clients{left:0;top:108px;width:780px;height:190px;background:var(--panel)}
  .client{position:absolute;top:92px;width:91px;height:61px;background:var(--white);display:flex;align-items:center;justify-content:center;gap:4px;font-family:"Roboto",sans-serif;font-weight:700;font-size:11px;color:#222;text-transform:uppercase}
  .client i{width:6px;height:6px;background:#222;display:block}
  .arrow{position:absolute;top:119px;width:16px;height:16px;border-radius:50%;background:var(--cyan)}

  /* pricing */
  .plan{position:absolute;top:404px;width:161px;height:202px;border:1.5px solid}
  .plan-name{position:absolute;top:-11px;left:50%;transform:translateX(-50%);height:21px;padding:0 7px;color:var(--white);font-family:"Roboto",sans-serif;font-weight:700;font-size:17px;line-height:21px;text-transform:uppercase}
  .plan ul{list-style:none;position:absolute;top:19px;left:14px;right:14px}
  .plan li{height:21.6px;line-height:21px;text-align:center;font-size:8px;color:#444;border-bottom:1px solid #ddd}
  .plan li:last-child{border-bottom:none}
  .plan-price{position:absolute;left:0;right:0;bottom:0;height:72px;display:flex;align-items:center;justify-content:center;text-align:center;color:var(--white);font-family:"Roboto",sans-serif;font-weight:700;font-size:16px;line-height:21px}
  .bronze{border-color:var(--cyan)} .bronze .plan-name,.bronze .plan-price{background:var(--cyan)}
  .silver{border-color:var(--silver)} .silver .plan-name,.silver .plan-price{background:var(--silver)}
  .gold{border-color:var(--gold)} .gold .plan-name,.gold .plan-price{background:var(--gold)}

  /* blog */
  .blog{left:0;top:622px;width:780px;height:345px;background:var(--panel)}
  .feature{left:146px;top:710px;width:248px;height:221px;background:linear-gradient(120deg,#d9b48f 0%,#e9d6c4 45%,#b7c9dc 100%)}
  .feature-panel{left:146px;top:710px;width:132px;height:221px;background:rgba(40,190,232,.88);color:var(--white);padding:14px 14px 0 14px}
  .feature-panel h3{font-family:"Roboto",sans-serif;font-size:10.5px;line-height:12.5px;font-weight:700}
  .feature-panel p{font-size:7.5px;line-height:12px;margin-top:10px;opacity:.95}
  .feature-panel .date{font-size:7.5px;margin-top:8px}
  .feature-panel .more{font-size:7.5px;font-weight:700;margin-top:18px}
  .post{position:absolute;left:408px;width:248px;height:72px;border-bottom:1px solid #e0e0e0}
  .thumb{position:absolute;left:0;top:0;width:46px;height:46px;background:linear-gradient(135deg,#e4d4c2,#b9cde0)}
  .thumb-date{position:absolute;left:0;top:46px;width:46px;height:9px;background:var(--cyan);color:var(--white);font-size:6.5px;font-weight:700;text-align:center;line-height:9px}
  .post h4{position:absolute;left:55px;top:4px;font-family:"Carlito",sans-serif;font-size:8.5px;font-weight:700;color:var(--cyan)}
  .post p{position:absolute;left:55px;top:15px;width:190px;font-size:7px;line-height:12px;color:#333}
  .post .meta{position:absolute;left:55px;top:54px;font-size:5.8px;color:var(--cyan)}

  /* contact */
  .contact{left:0;top:967px;width:780px;height:190px;background:var(--cyan)}
  .contact .section-title{color:var(--white)}
  .contact-item{position:absolute;top:1060px;width:140px;text-align:center;color:var(--white);font-size:7.5px;font-weight:700}
  .contact-item svg{display:block;margin:0 auto 10px}

  /* footer */
  .footer{left:0;top:1157px;width:780px;height:43px;background:var(--cyan-light)}
  .social{position:absolute;top:1176px;width:11px;height:11px;border-radius:50%;background:rgba(255,255,255,.45)}
</style>
</head>
<body>

<!-- Testimonials -->
<section class="abs testimonials" role="img" aria-label="Photo of a smiling customer giving a thumbs up, tinted blue"></section>
<div class="avatar" style="left:142px;top:2px" role="img" aria-label="Portrait of Martin Hale"></div>
<div class="reviewer" style="left:198px;top:18px">Martin Hale<span>Apartment Owner</span></div>
<div class="avatar" style="left:411px;top:2px" role="img" aria-label="Portrait of Owen Pryce"></div>
<div class="reviewer" style="left:467px;top:18px">Owen Pryce</div>
<div class="dot active" style="left:390px"></div>
<div class="dot" style="left:401px"></div>
<div class="dot" style="left:412px"></div>

<!-- Clients -->
<section class="abs clients">
  <h2 class="section-title" style="top:32px">OUR CLIENTS</h2>
  <div class="abs" style="left:274px;top:54px;width:260px;height:1px;background:#dcdcdc"></div>
  <svg class="wave" style="left:364px;top:51px" viewBox="0 0 40 6"><path d="M1 3 Q5.5 0 10 3 T19 3 T28 3 T39 3" fill="none" stroke="#1cb9e8" stroke-width="2"/></svg>
  <div class="arrow" style="left:124px"><svg width="16" height="16" viewBox="0 0 16 16"><path d="M9.5 4.5 6 8l3.5 3.5" fill="none" stroke="#fff" stroke-width="1.6"/></svg></div>
  <div class="client" style="left:150px">Oakline Co.</div>
  <div class="client" style="left:255px"><i></i>Fernway</div>
  <div class="client" style="left:359px">Kestrel Port</div>
  <div class="client" style="left:464px">Harbour Mill</div>
  <div class="client" style="left:568px">Stonebeck</div>
  <div class="arrow" style="left:668px"><svg width="16" height="16" viewBox="0 0 16 16"><path d="M6.5 4.5 10 8l-3.5 3.5" fill="none" stroke="#fff" stroke-width="1.6"/></svg></div>
</section>

<!-- Pricing -->
<h2 class="section-title" style="top:332px">PRICING</h2>
<svg class="wave" style="left:384px;top:353px" viewBox="0 0 40 6"><path d="M1 3 Q5.5 0 10 3 T19 3 T28 3 T39 3" fill="none" stroke="#1cb9e8" stroke-width="2"/></svg>

<div class="plan bronze" style="left:150px">
  <div class="plan-name">Bronze</div>
  <ul><li>Upholstery Cleaning</li><li>Carpet Cleaning</li><li>House Cleaning</li><li>Apartment Cleaning</li><li>Building Cleaning</li></ul>
  <div class="plan-price">£50<br>/month</div>
</div>
<div class="plan silver" style="left:324px">
  <div class="plan-name">Silver</div>
  <ul><li>Upholstery Cleaning</li><li>Carpet Cleaning</li><li>House Cleaning</li><li>Apartment Cleaning</li><li>Building Cleaning</li></ul>
  <div class="plan-price">£100<br>/month</div>
</div>
<div class="plan gold" style="left:498px">
  <div class="plan-name">Gold</div>
  <ul><li>Upholstery Cleaning</li><li>Carpet Cleaning</li><li>House Cleaning</li><li>Apartment Cleaning</li><li>Building Cleaning</li></ul>
  <div class="plan-price">£200<br>/month</div>
</div>

<!-- Blog -->
<section class="abs blog">
  <h2 class="section-title" style="top:28px;left:-3px">LATEST BLOG</h2>
  <svg class="wave" style="left:381px;top:48px" viewBox="0 0 40 6"><path d="M1 3 Q5.5 0 10 3 T19 3 T28 3 T39 3" fill="none" stroke="#1cb9e8" stroke-width="2"/></svg>
</section>
<div class="abs feature" role="img" aria-label="Photo of two cleaners wiping a window"></div>
<article class="abs feature-panel">
  <h3>5 Tips Of Hiring Office Cleaners</h3>
  <p>Mauris varius porttitor suscipit. Quisque justo tortor, convallis id elit vitae, posuere ullamcorper ante. Sed in magna viverra, fermentum...</p>
  <div class="date">October 25, 2015</div>
  <div class="more">Read More</div>
</article>

<article class="post" style="top:710px;height:80px">
  <div class="thumb" role="img" aria-label="Photo of a smiling cleaner"></div>
  <div class="thumb-date">25 Oct 2015</div>
  <h4>5 Tips Of Hiring Office Cleaners</h4>
  <p>Mauris varius porttitor suscipit. Quisque justo tortor, convallis id elit vitae, posuere ullamcorper ante. Sed in magna viverra, fermentum...</p>
  <div class="meta">0 Comments &nbsp;/&nbsp; Tips , &nbsp;Wash &nbsp;/&nbsp; Read More</div>
</article>
<article class="post" style="top:790px;height:80px">
  <div class="thumb" role="img" aria-label="Photo of team hands joined together"></div>
  <div class="thumb-date">24 Oct 2015</div>
  <h4>Cleaning Team Is Ready To Work</h4>
  <p>Mauris varius porttitor suscipit. Quisque justo tortor, convallis id elit vitae, posuere ullamcorper ante. Sed in magna viverra, fermentum...</p>
  <div class="meta">0 Comments &nbsp;/&nbsp; Uncategorized &nbsp;/&nbsp; Read More</div>
</article>
<article class="post" style="top:870px;height:62px;border-bottom:none">
  <div class="thumb" role="img" aria-label="Photo of a tidy apartment interior"></div>
  <div class="thumb-date">23 Oct 2015</div>
  <h4>10 Tips Cleaning Your Apartment</h4>
  <p>Mauris varius porttitor suscipit. Quisque justo tortor, convallis id elit vitae, posuere ullamcorper ante. Sed in magna viverra, fermentum...</p>
  <div class="meta">0 Comments &nbsp;/&nbsp; Tips &nbsp;/&nbsp; Read More</div>
</article>

<!-- Contact -->
<section class="abs contact">
  <h2 class="section-title" style="top:36px">CONTACT US</h2>
  <div class="abs" style="left:266px;top:59px;width:269px;height:1px;background:rgba(255,255,255,.85)"></div>
  <svg class="wave" style="left:380px;top:56px" viewBox="0 0 40 6"><path d="M1 3 Q5.5 0 10 3 T19 3 T28 3 T39 3" fill="none" stroke="#fff" stroke-width="2"/></svg>
</section>
<div class="contact-item" style="left:151px">
  <svg width="16" height="16" viewBox="0 0 16 16"><path d="M3.5 2 6 4.5 4.8 6.3c.8 1.8 2.3 3.4 4.2 4.3L10.8 9.4 13.5 12l-1.6 2c-5-.6-9.3-4.9-9.9-10z" fill="none" stroke="#fff" stroke-width="1"/></svg>
  01632 960451
</div>
<div class="contact-item" style="left:330px">
  <svg width="16" height="18" viewBox="0 0 16 18"><path d="M8 17S2.5 10.5 2.5 6.5a5.5 5.5 0 0 1 11 0C13.5 10.5 8 17 8 17z" fill="none" stroke="#fff" stroke-width="1"/><circle cx="8" cy="6.5" r="2" fill="none" stroke="#fff" stroke-width="1"/></svg>
  Ashbridge
</div>
<div class="contact-item" style="left:509px">
  <svg width="16" height="16" viewBox="0 0 16 16"><rect x="1.5" y="3.5" width="13" height="9" fill="none" stroke="#fff" stroke-width="1"/><path d="M1.5 3.5 8 9l6.5-5.5" fill="none" stroke="#fff" stroke-width="1"/></svg>
  info@brightmeadow.co.uk
</div>

<!-- Footer -->
<footer class="abs footer"></footer>
<span class="social" style="left:333px"></span>
<span class="social" style="left:354px"></span>
<span class="social" style="left:374px"></span>
<span class="social" style="left:395px"></span>
<span class="social" style="left:416px"></span>
<span class="social" style="left:436px"></span>
<span class="social" style="left:457px"></span>

</body>
</html>
```